SINGLE PAGE WEBSITE needed for Haunted-House Style Horror Event!

PROJECT:
Single page website to advertise "Bolting Shadows"

ABOUT BOLTING SHADOWS:
Bolting Shadows is a Horror Experience event, that will be held on June 1st 2019 at The Ember Playhouse in Sydney.

At the event, patrons will enter 6 different rooms and have a horror experience in each one.

There's a bar on-site for them to drink as well.

NEEDS FOR THE WEBSITE:
1. Video banner at top, and scrolling photos after video finishes, and text over the top of the video with the name and date of the event
eg.
"A Night of Immersive Horror Experiences"
"The Ember Playhouse | June 1st, 2019"

2. Multiple Book Now buttons on the page, which will link to an external booking platform

3. It should say somewhere "Produced by [MARBLE LANTERN PRODUCTIONS LOGO]"

4. A "Next Steps" section that has the steps for them to complete, such as
- Purchase your ticket HERE for one of our waves
- Rock up at the Ember Playhouse on June 1st at your wave time
- Experience each of our 6 Interactive Horror Rooms
- Grab some drinks at the bar, a bite to eat, and enjoy a fantastic night out!

Other things that should be included somewhere:
- Testimonials
- FAQs (maybe as a dropdown, so it doesn't take up much space?)
- Contact Form on Footer

- - - -

Images, logos, and more attached!

Industry/Entity Type

Events

Coding

Coded - Design and coding required

Number of Pages Required

1 page

Requirements
Nice to have
• 1. Video banner at top, and scrolling photos after video finishes, and text over the top of the video with the name and date of the event
• eg.
• "A Night of Immersive Horror Experiences"
• "The Ember Playhouse | June 1st, 2019"
• 2. multiple Book Now buttons on the page, which will link to an external booking platform
• 3. It should say somewhere "Produced by [Marble Lantern Productions LOGO]" with the Marble Lantern logo
• 4. A "Next Steps" section that has the steps for them to complete, such as
• - Purchase your ticket HERE for one of our waves
• - Rock up at the Ember Playhouse on June 1st at your wave time
• - Experience each of our 6 Interactive Horror Rooms
• - Grab some drinks at the bar, a bite to eat, and enjoy a fantastic night out!
• Other things that should be included somewhere:
• - Testimonials
• - FAQs (maybe as a dropdown, so it doesn't take up much space?)
• - Contact Form on Footer

```html
<!DOCTYPE html>
<html lang="en">
<head>
<meta charset="utf-8">
<title>Bolting Shadows — A Night of Immersive Horror Experiences</title>
<link rel="stylesheet" href="https://fonts.googleapis.com/css2?family=Montserrat:wght@600;700&family=Poppins:wght@400;500;600;700;800&family=Freckle+Face&display=swap">
<style>
:root{
  --green:#8cbf26;
  --green-dark:#6f9a1c;
  --ink:#1b1b1b;
  --text:#3a3a3a;
  --muted:#6a6a6a;
  --field:#eeeeee;
  --footer:#141414;
  --white:#ffffff;
}
*{box-sizing:border-box;margin:0;padding:0}
html,body{width:1200px;height:3758px;overflow:hidden}
body{position:relative;background:var(--white);font-family:'Poppins',sans-serif;color:var(--text)}
.abs{position:absolute}
.display{font-family:'Freckle Face',cursive}

/* header */
.site-header{left:0;top:0;width:1200px;height:133px;background:var(--white)}
.brand{display:flex;align-items:center;gap:14px;font-family:'Poppins',sans-serif;font-weight:800;color:var(--ink);text-transform:uppercase;letter-spacing:1px}
.brand-mark{width:30px;height:30px;background:var(--green)}
.site-header .brand{left:75px;top:50px;font-size:26px}
.main-nav a{position:absolute;top:58px;font-size:18px;color:#333;text-decoration:none;font-weight:500}
.main-nav .active::after{content:"";position:absolute;left:0;right:0;top:56px;height:3px;background:var(--green)}

/* hero */
.hero{left:0;top:133px;width:1200px;height:581px;background:radial-gradient(ellipse at 50% 40%,#5a5550 0%,#2c2a28 55%,#121110 100%)}
.hero-title{left:0;top:177px;width:1200px;text-align:center;font-family:'Montserrat',sans-serif;font-weight:600;font-size:50px;line-height:58px;color:var(--white)}
.hero-sub{left:0;top:307px;width:1200px;text-align:center;font-size:40px;line-height:48px;color:var(--green)}
.btn{display:flex;align-items:center;justify-content:center;gap:10px;background:var(--green);color:var(--ink);font-weight:600;font-size:18px;border-radius:6px;text-decoration:none}
.hero .btn{left:523px;top:373px;width:155px;height:46px}
.play{width:28px;height:28px;border-radius:50%;background:var(--ink);display:flex;align-items:center;justify-content:center}

/* producer */
.produced-label{left:0;top:748px;width:1200px;text-align:center;font-weight:600;font-size:17px;color:var(--ink)}
.producer-name{left:0;top:820px;width:1200px;justify-content:center;font-size:30px;color:#3b3f73}
.producer-name .brand-mark{background:#9aa0d8}

/* how it works */
.section-title{left:0;width:1200px;text-align:center;font-size:42px;line-height:52px}
.how-title{top:952px;color:var(--green)}
.step-icon{width:180px;height:180px;border-radius:50%;border:9px solid var(--green);background:radial-gradient(circle,#f5d37a 0%,#f0f0f0 45%,#ffffff 70%)}
.step-text{width:190px;text-align:center;font-size:15px;font-weight:600;line-height:26px;color:#333}
.steps .btn{left:521px;top:1375px;width:155px;height:47px;font-size:17px}

/* testimonials */
.testimonials{left:0;top:1478px;width:1200px;height:591px;background:linear-gradient(90deg,#7ea825 0%,#93b92f 50%,#7a9f22 100%)}
.testimonials-photo{left:0;top:0;width:1200px;height:591px;background:radial-gradient(ellipse at 20% 40%,rgba(200,220,120,.35),transparent 50%),radial-gradient(ellipse at 80% 30%,rgba(210,230,140,.35),transparent 45%)}
.test-title{top:68px;color:var(--ink)}
.quote-card{top:195px;width:328px;height:268px;background:var(--white);padding:62px 34px 0 34px;font-size:13.5px;line-height:28px;color:#555}
.quote-mark{position:absolute;left:35px;top:-7px;width:31px;height:31px;background:var(--ink);color:var(--white);font-family:Georgia,serif;font-size:28px;line-height:38px;text-align:center}
.quote-author{font-weight:700;color:var(--ink);margin-top:4px}
.slider-arrows{left:572px;top:502px;width:56px;height:26px}

/* faq */
.faq-title{top:2125px;color:var(--ink)}
.faq-item{left:88px;width:1052px;border:1px solid #d8d8d8;background:var(--white)}
.faq-q{height:66px;display:flex;align-items:center;padding-left:20px;position:relative}
.faq-q .q{font-family:'Poppins',sans-serif;font-weight:800;font-size:34px;color:var(--green);width:52px}
.faq-q .txt{font-weight:600;font-size:15.5px;color:var(--green);text-transform:uppercase}
.faq-q svg{position:absolute;right:22px;top:24px}
.faq-a{background:#f1f1f1;border-top:1px solid #d8d8d8;height:94px;padding:26px 70px 0 70px;font-size:13.5px;line-height:24px;color:#555}
.faq .btn{left:523px;top:2766px;width:183px;height:50px;font-size:16px;text-transform:uppercase}

/* footer */
.site-footer{left:0;top:2906px;width:1200px;height:701px;background:radial-gradient(ellipse at 25% 60%,#2b2b2b 0%,var(--footer) 55%,#0b0b0b 100%)}
.footer-h{font-weight:700;font-size:38px;color:var(--white)}
.info-line{display:flex;align-items:center;gap:14px;font-size:15px;color:var(--white)}
.quick-links a{position:absolute;left:124px;font-size:15px;color:var(--white);text-decoration:none}
.quick-links svg{position:absolute;left:92px}
.footer-divider{left:371px;top:74px;width:2px;height:552px;background:var(--green-dark)}
.field-label{font-size:15px;color:var(--white)}
.field{background:var(--field);height:45px}
.site-footer .btn{height:50px;font-size:17px}
.to-top{left:586px;top:3579px;width:56px;height:56px;border-radius:50%;background:var(--ink);border:3px solid var(--white);display:flex;align-items:center;justify-content:center}

/* bottom bar */
.bottom-bar{left:0;top:3607px;width:1200px;height:151px;background:var(--white)}
.bottom-bar .brand{left:72px;top:52px;font-size:26px}
.social{top:44px;width:22px;height:22px;border-radius:50%;background:var(--ink)}
.copyright{left:870px;top:82px;font-size:15px;color:#333}
</style>
</head>
<body>

<header class="site-header abs">
  <div class="brand abs"><span class="brand-mark"></span>Bolting Shadows</div>
  <nav class="main-nav">
    <a class="active" style="left:441px" href="#">Home</a>
    <a style="left:536px" href="#">About Us</a>
    <a style="left:659px" href="#">How it Works</a>
    <a style="left:811px" href="#">Testimonials</a>
    <a style="left:958px" href="#">FAQ</a>
    <a style="left:1032px" href="#">Contact us</a>
  </nav>
</header>

<section class="hero abs" role="img" aria-label="Dark hooded figure surrounded by skulls — video banner">
  <h1 class="hero-title abs">A Night of Immersive<br>Horror Experiences</h1>
  <p class="hero-sub abs display">The Ember Playhouse | June 1st, 2019</p>
  <a class="btn abs" href="#"><span class="play"><svg width="12" height="12" viewBox="0 0 12 12"><path d="M3 1l8 5-8 5z" fill="#fff"/></svg></span>Play Now</a>
</section>

<p class="produced-label abs">Produced by</p>
<div class="brand producer-name abs"><span class="brand-mark"></span>Marble Lantern Productions</div>

<section class="steps">
  <h2 class="section-title how-title abs display">HOW IT WORKS</h2>
  <div class="step-icon abs" style="left:110px;top:1065px" role="img" aria-label="Ticket and cash icon"></div>
  <div class="step-icon abs" style="left:378px;top:1065px" role="img" aria-label="Theatre stage icon"></div>
  <div class="step-icon abs" style="left:644px;top:1065px" role="img" aria-label="Zombie icon"></div>
  <div class="step-icon abs" style="left:912px;top:1065px" role="img" aria-label="Bottles and drinks icon"></div>
  <p class="step-text abs" style="left:105px;top:1248px">Purchase your ticket HERE for one of our waves</p>
  <p class="step-text abs" style="left:373px;top:1248px">Rock up at the Ember Playhouse on June 1st at your wave time</p>
  <p class="step-text abs" style="left:639px;top:1248px">Experience each of our 6 Interactive Horror Rooms</p>
  <p class="step-text abs" style="left:907px;top:1248px">Grab some drinks at the bar, a bite to eat, and enjoy a fantastic night out!</p>
  <a class="btn abs" href="#">Book Now</a>
</section>

<section class="testimonials abs">
  <div class="testimonials-photo abs" role="img" aria-label="Frightened faces washed in green"></div>
  <h2 class="section-title test-title abs display">TESTIMONIALS</h2>
  <article class="quote-card abs" style="left:75px"><span class="quote-mark">“</span>“Sed ut perspiciatis unde omnis iste natus error sit voluptatem accusan-tium doloremque laudantium, totam rem aperiam, eaque ipsa quae ab illo inventore veritatis et quasi architecto beatae vitae dicta sunt ”<p class="quote-author">- Mara</p></article>
  <article class="quote-card abs" style="left:436px"><span class="quote-mark">“</span>“Sed ut perspiciatis unde omnis iste natus error sit voluptatem accusan-tium doloremque laudantium, totam rem aperiam, eaque ipsa quae ab illo inventore veritatis et quasi architecto beatae vitae dicta sunt ”<p class="quote-author">- Mara</p></article>
  <article class="quote-card abs" style="left:797px"><span class="quote-mark">“</span>“Sed ut perspiciatis unde omnis iste natus error sit voluptatem accusan-tium doloremque laudantium, totam rem aperiam, eaque ipsa quae ab illo inventore veritatis et quasi architecto beatae vitae dicta sunt ”<p class="quote-author">- Mara</p></article>
  <svg class="slider-arrows abs" viewBox="0 0 56 26"><path d="M14 5l-8 8 8 8M42 5l8 8-8 8" stroke="#1b1b1b" stroke-width="4" fill="none"/></svg>
</section>

<section class="faq">
  <h2 class="section-title faq-title abs display">FAQ</h2>
  <div class="faq-item abs" style="top:2222px">
    <div class="faq-q"><span class="q">Q.</span><span class="txt">Neque porro quisquam est qui dolorem ipsum quia dolor sit amet?</span><svg width="14" height="10" viewBox="0 0 14 10"><path d="M2 2l5 5 5-5" stroke="#333" stroke-width="2" fill="none"/></svg></div>
    <div class="faq-a">Sed ut perspiciatis unde omnis iste natus error sit voluptatem accusantium doloremque laudantium, totam rem aperiam, eaque ipsa quae ab illo inventore veritatis et quasi architecto beatae</div>
  </div>
  <div class="faq-item abs" style="top:2397px"><div class="faq-q"><span class="q">Q.</span><span class="txt">Neque porro quisquam est qui dolorem ipsum quia dolor sit amet?</span><svg width="10" height="14" viewBox="0 0 10 14"><path d="M2 2l5 5-5 5" stroke="#333" stroke-width="2" fill="none"/></svg></div></div>
  <div class="faq-item abs" style="top:2482px"><div class="faq-q"><span class="q">Q.</span><span class="txt">Lorem Ipsum is simply dummy text of the printing and typesetting?</span><svg width="10" height="14" viewBox="0 0 10 14"><path d="M2 2l5 5-5 5" stroke="#333" stroke-width="2" fill="none"/></svg></div></div>
  <div class="faq-item abs" style="top:2566px"><div class="faq-q"><span class="q">Q.</span><span class="txt">Sed ut perspiciatis unde omnis iste natus error sit voluptatem?</span><svg width="10" height="14" viewBox="0 0 10 14"><path d="M2 2l5 5-5 5" stroke="#333" stroke-width="2" fill="none"/></svg></div></div>
  <div class="faq-item abs" style="top:2650px"><div class="faq-q"><span class="q">Q.</span><span class="txt">Lorem Ipsum is simply dummy text of the printing and typesetting?</span><svg width="10" height="14" viewBox="0 0 10 14"><path d="M2 2l5 5-5 5" stroke="#333" stroke-width="2" fill="none"/></svg></div></div>
  <a class="btn abs" href="#">View More</a>
</section>

<footer class="site-footer abs" role="img" aria-label="Dim horror scene behind footer">
  <h3 class="footer-h abs" style="left:90px;top:54px">Locations</h3>
  <p class="info-line abs" style="left:90px;top:166px"><svg width="14" height="18" viewBox="0 0 14 18"><path d="M7 0a7 7 0 0 0-7 7c0 5 7 11 7 11s7-6 7-11a7 7 0 0 0-7-7zm0 10a3 3 0 1 1 0-6 3 3 0 0 1 0 6z" fill="#fff"/></svg>42 Hollow Lane</p>
  <p class="info-line abs" style="left:118px;top:194px">Marrow Bay, NSW 2199</p>
  <p class="info-line abs" style="left:90px;top:224px"><svg width="14" height="14" viewBox="0 0 14 14"><path d="M3 0l3 3-2 2c1 2 3 4 5 5l2-2 3 3-2 3C6 14 0 8 0 2z" fill="#fff"/></svg>(02) 5550 1934</p>
  <p class="info-line abs" style="left:90px;top:252px"><svg width="14" height="11" viewBox="0 0 14 11"><path d="M0 0h14v11H0zM0 0l7 6 7-6" fill="#fff" stroke="#141414" stroke-width="1"/></svg>hello@boltingshadows.test</p>
  <h3 class="footer-h abs" style="left:90px;top:304px">Quick Links</h3>
  <nav class="quick-links">
    <svg style="top:388px" width="8" height="12" viewBox="0 0 8 12"><path d="M1 1l5 5-5 5" stroke="#fff" stroke-width="2" fill="none"/></svg><a style="top:381px" href="#">Home</a>
    <svg style="top:421px" width="8" height="12" viewBox="0 0 8 12"><path d="M1 1l5 5-5 5" stroke="#fff" stroke-width="2" fill="none"/></svg><a style="top:414px" href="#">About Us</a>
    <svg style="top:455px" width="8" height="12" viewBox="0 0 8 12"><path d="M1 1l5 5-5 5" stroke="#fff" stroke-width="2" fill="none"/></svg><a style="top:448px" href="#">How it Works</a>
    <svg style="top:488px" width="8" height="12" viewBox="0 0 8 12"><path d="M1 1l5 5-5 5" stroke="#fff" stroke-width="2" fill="none"/></svg><a style="top:481px" href="#">Testimonials</a>
    <svg style="top:522px" width="8" height="12" viewBox="0 0 8 12"><path d="M1 1l5 5-5 5" stroke="#fff" stroke-width="2" fill="none"/></svg><a style="top:515px" href="#">FAQ</a>
    <svg style="top:555px" width="8" height="12" viewBox="0 0 8 12"><path d="M1 1l5 5-5 5" stroke="#fff" stroke-width="2" fill="none"/></svg><a style="top:548px" href="#">Contact Us</a>
  </nav>
  <a class="btn abs" style="left:90px;top:594px;width:155px" href="#">Book Now</a>
  <div class="footer-divider abs"></div>

  <h3 class="footer-h abs" style="left:416px;top:54px">Contact Us</h3>
  <p class="field-label abs" style="left:424px;top:148px">First Name</p>
  <p class="field-label abs" style="left:795px;top:148px">Last Name</p>
  <div class="field abs" style="left:421px;top:180px;width:348px"></div>
  <div class="field abs" style="left:789px;top:180px;width:351px"></div>
  <p class="field-label abs" style="left:424px;top:241px">Email</p>
  <p class="field-label abs" style="left:795px;top:241px">Phone</p>
  <div class="field abs" style="left:421px;top:275px;width:348px"></div>
  <div class="field abs" style="left:789px;top:275px;width:351px"></div>
  <p class="field-label abs" style="left:424px;top:333px">Subject</p>
  <div class="field abs" style="left:421px;top:368px;width:719px"></div>
  <p class="field-label abs" style="left:424px;top:426px">Message</p>
  <div class="field abs" style="left:421px;top:458px;width:719px;height:108px"></div>
  <a class="btn abs" style="left:416px;top:584px;width:145px;text-transform:uppercase;font-weight:700" href="#">Submit</a>
</footer>

<div class="bottom-bar abs">
  <div class="brand abs"><span class="brand-mark"></span>Bolting Shadows</div>
  <span class="social abs" style="left:961px"></span>
  <span class="social abs" style="left:1004px"></span>
  <span class="social abs" style="left:1049px"></span>
  <span class="social abs" style="left:1096px"></span>
  <p class="copyright abs">© 2019 &nbsp;|&nbsp; www.boltingshadows.test &nbsp;&nbsp;&nbsp;&nbsp; M1</p>
</div>

<a class="to-top abs" href="#"><svg width="16" height="10" viewBox="0 0 16 10"><path d="M2 8l6-6 6 6" stroke="#fff" stroke-width="3" fill="none"/></svg></a>

</body>
</html>
```